Simple, elegant, business card design required

Hi designers,I am looking for a simple yet elegant business card design.

Please make use of my logo (attached); you are free to tweak the logo should you wish to do so.

Our business is involved in many different fields - almost all of them involved in some form of "design", so that's really one of the key things I want to portray. I do not wish to specify which field of design, exactly.

I prefer white on black (or just monochromatic), but if you have a different, creative idea, I am open to that too.

You can use artsy photographs provided that you have the license to use those. Please feel free to ask me any questions.
Updates

Project Deadline Extended Reason: Small extension for potential revisions. Did not get the time to provide as much feedback as I can. Added Wednesday, July 09, 2014

Target Market(s)

High-end customers looking for design consultancy

Industry/Entity Type

Business

Contact Information for Business Card

Name: Gareth Moonfield
Position: Creative Director
Mobile: +155603928174
Address: Barrow Lane, Ellsworth Vale, Warwickshire GL12 4RT
Website: torvakest.com (not launched yet)

Requirements
Must have
• Design layout must be clean, original, and text must be readable when printed.
Should not have
• ~ No business card templates please. Anyone using this will be reported.
• ~ Please don't spam entries.

```html
<!DOCTYPE html>
<html lang="en">
<head>
<meta charset="utf-8">
<title>Torvakest Business Cards</title>
<link rel="stylesheet" href="https://fonts.googleapis.com/css2?family=Open+Sans:wght@400;600;700&display=swap">
<style>
  :root {
    --backdrop: #7a4a24;
    --ink: #000000;
    --paper: #f4f8f4;
    --white: #ffffff;
    --text-dark: #111111;
  }
  * { margin: 0; padding: 0; box-sizing: border-box; }
  html, body {
    width: 1200px;
    height: 771px;
    overflow: hidden;
  }
  body {
    position: relative;
    background: var(--backdrop);
    font-family: "Open Sans", Arial, sans-serif;
  }

  .card {
    position: absolute;
    width: 600px;
    height: 342px;
    overflow: hidden;
    box-shadow: 0 6px 18px rgba(0, 0, 0, 0.35);
  }

  /* Front card */
  .card-front {
    left: 128px;
    top: 30px;
    background: var(--ink);
    color: var(--white);
  }
  .front-band {
    position: absolute;
    left: 0;
    top: 0;
    width: 600px;
    height: 342px;
  }
  .brand {
    position: absolute;
    display: flex;
    align-items: center;
    font-weight: 400;
    white-space: nowrap;
    line-height: 1;
  }
  .brand-dot {
    display: block;
    flex: none;
    border-radius: 50%;
    background: currentColor;
  }
  .card-front .brand {
    left: 28px;
    top: 52px;
    gap: 57px;
    font-size: 25px;
    letter-spacing: 0.2em;
    color: var(--white);
  }
  .card-front .brand-dot { width: 22px; height: 22px; }

  .contact-list {
    position: absolute;
    left: 30px;
    top: 172px;
    list-style: none;
    font-size: 14px;
    line-height: 22px;
  }
  .contact-list li {
    display: flex;
    align-items: center;
    gap: 10px;
  }
  .contact-icon { width: 12px; height: 14px; flex: none; }

  .address {
    position: absolute;
    left: 30px;
    top: 253px;
    font-size: 14px;
    line-height: 22px;
    font-style: normal;
    font-weight: 600;
  }

  .person {
    position: absolute;
    left: 384px;
    top: 288px;
    width: 170px;
    text-align: center;
    color: var(--text-dark);
    font-size: 14px;
    line-height: 22px;
  }
  .person-name { font-weight: 700; }
  .person-role { font-weight: 400; }

  /* Back card */
  .card-back {
    left: 474px;
    top: 400px;
    background: var(--paper);
  }
  .back-panel {
    position: absolute;
    left: 0;
    top: 0;
    width: 231px;
    height: 342px;
    background: var(--ink);
  }
  .card-back .brand {
    left: 171px;
    top: 158px;
    gap: 59px;
    font-size: 30px;
    letter-spacing: 0.18em;
    color: var(--ink);
  }
  .card-back .brand-dot {
    width: 22px;
    height: 22px;
    background: var(--white);
  }
</style>
</head>
<body>

  <section class="card card-front" aria-label="Business card front">
    <svg class="front-band" viewBox="0 0 600 342" aria-hidden="true">
      <path d="M0 312 H300 C340 312 350 285 395 285 H600 V342 H0 Z" fill="var(--paper)"/>
    </svg>

    <div class="brand"><span class="brand-dot"></span>TORVAKEST</div>

    <ul class="contact-list">
      <li>
        <svg class="contact-icon" viewBox="0 0 12 14" aria-hidden="true">
          <rect x="2.5" y="0.8" width="7" height="12.4" rx="1.2" fill="none" stroke="#fff" stroke-width="1.2"/>
          <line x1="5" y1="11" x2="7" y2="11" stroke="#fff" stroke-width="1"/>
        </svg>
        <span>+155603928174</span>
      </li>
      <li>
        <svg class="contact-icon" viewBox="0 0 12 14" aria-hidden="true">
          <circle cx="6" cy="7" r="4.6" fill="none" stroke="#fff" stroke-width="1"/>
          <ellipse cx="6" cy="7" rx="2" ry="4.6" fill="none" stroke="#fff" stroke-width="0.8"/>
          <line x1="1.4" y1="7" x2="10.6" y2="7" stroke="#fff" stroke-width="0.8"/>
        </svg>
        <span>torvakest.com</span>
      </li>
    </ul>

    <address class="address">
      Barrow Lane, Ellsworth Vale<br>
      Brackenshire GL12 4RT
    </address>

    <div class="person">
      <p class="person-name">Gareth Moonfield</p>
      <p class="person-role">Creative Director</p>
    </div>
  </section>

  <section class="card card-back" aria-label="Business card back">
    <div class="back-panel"></div>
    <div class="brand"><span class="brand-dot"></span>TORVAKEST</div>
  </section>

</body>
</html>
```